Postcard Design

I'm hosting a retreat in Tuscany tag line ideas for front: "nourish your soul with a taste of Tuscany" or "Savor the sweet life and Nourish your soul with a taste of Tuscany" here is the pertinent info- trip date: September 5-12, 2015 number:1.877.384.2951 e/m:Info@WillowmereRetreats.example Web address:www.WillowmereRetreats.example
What's included:
• 7 nights Accommodations in beautiful Villa
• All Meals and Snacks included
• Special Wine tasting Excursion in Chianti
• Guided Tour of Siena
• Hands on Cooking Class at the villa
• Yoga, Meditation walks, Journaling
Something like this should be on back lower right side: Spaces Limited Reserve Yours Today!
Other wording ideas for back: Renew your spirit in the quiet beauty of the Tuscan landscape (maybe above what's included)
This can be near the "spaces limited" =Invest in your health, spirit and well-being *airfare not included. See website for details
More ideas/maybe a better way to word all this??:
Welcome to "la Willowmere" (The sweet life)
Have you always wanted to travel to Italy? Want to experience the culture in a special way you couldn't enjoy as a typical tourist? This is the trip you've been waiting for. Life is too short to wait any longer!
Hosts show with pictures:
Lise Karen Bouchard woman w/dark hair headshot
Retreat host
Sharing her love of Italy's beautiful culture with you is her special gift
And
Greta Halvorsen
Personal wellness consultant
Yoga, Meditation, Asana, Reiki, Pilates

I included a photo of the current postcard I made front & back. You can also visit my website to get an idea of my style. I'm hoping you can make me a postcard that's more tantalizing, and will get me some clients! I will include some extra photos and feel free to use your own stock images... anything to help! Feel free to change up wording to make it more appealing, welcoming and make people chose to go on retreat with me instead the hundreds of other retreats out there.
Thank you
Lise Karen

```html
<!DOCTYPE html>
<html lang="en">
<head>
<meta charset="utf-8">
<title>Willowmere Wellness Retreat – Postcard</title>
<link rel="stylesheet" href="https://fonts.googleapis.com/css2?family=Kalam:wght@400;700&family=Quicksand:wght@500;600;700&family=Marcellus+SC&display=swap">
<style>
:root{
  --page:#e9e4dd;
  --orange:#e5782a;
  --orange-light:#f3a43e;
  --orange-pale:#f8c98a;
  --cream:#fff6e6;
  --peach:#f6d4b6;
  --brown:#9a4615;
  --brown-dark:#6e2f0c;
  --sun:#f7dc7a;
  --white:#ffffff;
  --green:#6f9a3a;
  --green-light:#a9c65a;
  --sky:#a9cde8;
}
*{box-sizing:border-box;margin:0;padding:0}
html,body{width:1200px;height:800px;overflow:hidden}
body{background:var(--page);position:relative;font-family:"Quicksand",sans-serif;color:var(--brown)}
.card{position:absolute;background:var(--white);overflow:hidden;box-shadow:0 6px 18px rgba(0,0,0,.25)}
.photo{position:absolute}

/* ---------- back side ---------- */
.back{left:50px;top:50px;width:560px;height:405px}
.hosts{position:absolute;left:0;top:0;width:230px;height:405px;background:var(--white)}
.hosts-header{position:absolute;left:0;top:0;width:230px;height:52px;background:linear-gradient(90deg,var(--white),var(--sun) 50%,var(--white))}
.hosts-title{position:absolute;left:0;top:4px;width:230px;text-align:center;font-family:"Kalam",cursive;font-weight:700;font-size:30px;color:var(--brown-dark)}
.host-photo-1{left:4px;top:52px;width:106px;height:164px;background:linear-gradient(180deg,#b7a88f,#5b4636 60%,#e9e6e2)}
.host-photo-2{left:116px;top:52px;width:110px;height:164px;background:linear-gradient(180deg,#c9c4bd,#6e645c 55%,#463b33)}
.host-info{position:absolute;top:222px;width:113px;text-align:center}
.host-info.first{left:2px}
.host-info.second{left:116px}
.host-name{font-family:"Marcellus SC",serif;font-size:11px;color:var(--brown-dark);border-bottom:1px solid var(--brown);padding-bottom:2px;line-height:1.1}
.host-role{font-family:"Marcellus SC",serif;font-size:8px;color:var(--brown-dark);margin-top:2px}
.host-note{font-family:"Kalam",cursive;font-size:9px;line-height:1.2;color:var(--brown);margin-top:14px}
.hosts-sun{position:absolute;left:0;top:216px;width:230px;height:96px;background:radial-gradient(ellipse at 30% 50%,rgba(247,220,122,.55),rgba(255,255,255,0) 70%);z-index:0}
.host-info{z-index:1}
.reserve{position:absolute;left:0;top:312px;width:230px;height:64px;background:linear-gradient(180deg,var(--white),var(--peach));text-align:center;padding-top:8px;font-size:17px;font-weight:600;line-height:1.15;color:var(--brown)}
.email{position:absolute;left:0;top:378px;width:230px;display:flex;align-items:center;justify-content:center;gap:6px;font-size:11.5px;font-weight:600;color:var(--brown)}
.email svg{width:16px;height:12px}

.included{position:absolute;left:230px;top:0;width:330px;height:312px;background:linear-gradient(180deg,var(--orange),var(--orange-light) 70%,var(--orange-pale));color:var(--white)}
.included-lead{font-family:"Kalam",cursive;font-size:16px;line-height:1.2;text-align:center;padding:10px 14px 0;color:var(--cream)}
.included-list{list-style:none;margin:14px 0 0 22px}
.included-list li{position:relative;padding-left:20px;font-size:12.5px;font-weight:500;line-height:1.25;margin-bottom:7px;color:var(--white)}
.included-list li::before{content:"";position:absolute;left:0;top:3px;width:9px;height:9px;border-radius:50%;background:var(--cream)}
.included-close{position:absolute;left:0;bottom:8px;width:330px;text-align:center;font-family:"Kalam",cursive;font-size:15px;color:var(--brown-dark)}
.back-landscape{left:230px;top:312px;width:330px;height:93px;background:linear-gradient(180deg,#6a9a3e,#94c04d 50%,#3e6a22)}
.back-mark{position:absolute;left:380px;top:330px;width:100px;text-align:center;color:var(--white);font-size:14px;font-weight:600;line-height:1.1}
.back-mark small{display:block;font-size:7px;letter-spacing:1px;text-transform:uppercase}

/* ---------- front side ---------- */
.front{left:630px;top:330px;width:530px;height:420px}
.villa{left:0;top:0;width:262px;height:264px;background:linear-gradient(180deg,var(--sky) 0,#dbe9f2 28%,#c8a878 45%,#7fa24a 70%,#4d7a2a)}
.details{position:absolute;left:0;top:264px;width:262px;height:156px;text-align:center;padding-top:16px}
.date{font-size:22px;font-weight:600;line-height:1.1;color:var(--orange)}
.phone{display:flex;align-items:center;justify-content:center;gap:6px;margin-top:18px;font-size:14px;font-weight:600;color:var(--brown)}
.phone svg{width:16px;height:14px}
.web{margin-top:10px;font-size:13px;font-weight:600;color:var(--brown)}

.brand-panel{position:absolute;left:262px;top:0;width:268px;height:290px;background:linear-gradient(180deg,var(--orange),var(--orange-light) 75%,var(--orange-pale))}
.brand-sun{position:absolute;left:10px;top:50px;width:250px;height:110px;background:radial-gradient(ellipse at 55% 50%,rgba(214,110,20,.55),rgba(0,0,0,0) 70%)}
.brand-name{position:absolute;left:0;top:22px;width:268px;text-align:center;font-size:38px;font-weight:600;color:var(--cream);line-height:1}
.brand-sub{position:absolute;left:0;top:66px;width:268px;text-align:center;font-family:"Marcellus SC",serif;font-size:15px;letter-spacing:1px;color:var(--cream)}
.brand-rule{position:absolute;left:40px;top:88px;width:188px;height:1px;background:var(--cream)}
.tagline{position:absolute;left:0;top:176px;width:268px;text-align:center;font-family:"Kalam",cursive;font-size:15px;line-height:1.3;color:var(--brown-dark)}
.tagline strong{display:block;font-size:24px;font-weight:700;line-height:1.1}
.hills{left:262px;top:290px;width:136px;height:130px;background:linear-gradient(180deg,#8fb24c,#5a8a2c 50%,#a6b85a)}
.grove{left:398px;top:290px;width:132px;height:130px;background:linear-gradient(180deg,#d9d4bf,#9a9c6c 45%,#8a6f4c)}
</style>
</head>
<body>

<section class="card back" aria-label="Postcard back">
  <div class="hosts">
    <div class="hosts-header" role="img" aria-label="Soft sunflower decoration behind the heading"></div>
    <h2 class="hosts-title">Our Hosts:</h2>
    <div class="photo host-photo-1" role="img" aria-label="Headshot of retreat host Lise Karen Bouchard"></div>
    <div class="photo host-photo-2" role="img" aria-label="Greta Halvorsen in a yoga pose on a mountain trail"></div>
    <div class="hosts-sun" role="img" aria-label="Faint sunflower decoration"></div>
    <div class="host-info first">
      <p class="host-name">Lise Karen Bouchard</p>
      <p class="host-role">Retreat Host</p>
      <p class="host-note">Sharing her love of Italy's beautiful culture with you is her special gift</p>
    </div>
    <div class="host-info second">
      <p class="host-name">Greta Halvorsen</p>
      <p class="host-role">Personal Wellness Consultant</p>
      <p class="host-note">Yoga, Meditation, Asana, Reiki, Pilates</p>
    </div>
    <p class="reserve">Spaces limited<br>Reserve yours TODAY!</p>
    <p class="email">
      <svg viewBox="0 0 16 12" aria-hidden="true"><rect x="0.5" y="0.5" width="15" height="11" fill="none" stroke="#e5782a"/><path d="M0.5 0.5 L8 7 L15.5 0.5" fill="none" stroke="#e5782a"/></svg>
      Info@WillowmereRetreats.example
    </p>
  </div>

  <div class="included">
    <p class="included-lead">Renew your spirit in the quiet beauty<br>of the Tuscan landscape</p>
    <ul class="included-list">
      <li>7 nights Accommodations in<br>beautiful Villa</li>
      <li>All Meals and Snacks included</li>
      <li>Special Wine tasting Excursion<br>in Chianti</li>
      <li>Guided Tour of Siena</li>
      <li>Hands on Cooking Class at the villa</li>
      <li>Yoga, Meditation walks, Journaling</li>
    </ul>
    <p class="included-close">Invest in your health, spirit and well-being</p>
  </div>
  <div class="photo back-landscape" role="img" aria-label="Green Tuscan hills with a meditating woman at the right"></div>
  <p class="back-mark">Willowmere<small>Wellness Retreat</small></p>
</section>

<section class="card front" aria-label="Postcard front">
  <div class="photo villa" role="img" aria-label="Stone Tuscan villa with a pool among fields under a blue sky"></div>
  <div class="details">
    <p class="date">September 5-12<br>2015</p>
    <p class="phone">
      <svg viewBox="0 0 16 14" aria-hidden="true"><path d="M1 5 Q8 -1 15 5 L13 7 L11 5.5 L11 4 Q8 3 5 4 L5 5.5 L3 7 Z" fill="#c0581a"/><rect x="4" y="7" width="8" height="6" rx="1" fill="#c0581a"/></svg>
      1.877.384.2951
    </p>
    <p class="web">www.WillowmereRetreats.example</p>
  </div>

  <div class="brand-panel">
    <div class="brand-sun" role="img" aria-label="Sunflower decoration behind the retreat name"></div>
    <p class="brand-name">Willowmere</p>
    <p class="brand-sub">Wellness Retreat</p>
    <div class="brand-rule"></div>
    <p class="tagline">Savor the sweet life and<br>Nourish your soul with a taste of<strong>Tuscany</strong></p>
  </div>
  <div class="photo hills" role="img" aria-label="Rolling green Tuscan hills with cypress trees"></div>
  <div class="photo grove" role="img" aria-label="Woman doing a yoga balance pose in a tree grove"></div>
</section>

</body>
</html>
```